Redesign Login page

I want to redesign my login page to bring my 2 products closer together. I am only looking to redesign one login page, not 2.

For the logo, please make it solid and it can be black or white if helpful. I can also fine tune the logo if you get it close.

Coding

Coded - Design and coding required

Number of Pages Required

1 page

```html
<!DOCTYPE html>
<html lang="en">
<head>
<meta charset="utf-8">
<title>Brelvix – Log in</title>
<link rel="stylesheet" href="https://fonts.googleapis.com/css2?family=Inter:wght@400;500;600;700&display=swap">
<style>
  :root {
    --page-bg: #ffffff;
    --card-bg: #ffffff;
    --shadow: rgba(120, 110, 220, 0.12);
    --heading: #1b1350;
    --muted: #6b6589;
    --teal: #80bcbf;
    --teal-link: #5fa5a8;
    --signup: #2f5d56;
    --line-active: #80bcbf;
    --line: #ececf3;
  }
  * { box-sizing: border-box; margin: 0; padding: 0; }
  html, body {
    width: 1200px; height: 784px; overflow: hidden;
    background: var(--page-bg);
    font-family: "Inter", sans-serif;
  }
  .login-card {
    position: absolute; left: 23px; top: 5px; width: 1156px; height: 739px;
    background: var(--card-bg); border-radius: 24px;
    box-shadow: 0 14px 30px var(--shadow);
  }
  .login-form {
    position: absolute; left: 86px; top: 0; width: 374px; height: 100%;
  }
  .brand {
    position: absolute; top: 138px; left: 6px;
    display: flex; align-items: center; gap: 10px;
    font-size: 44px; font-weight: 700; color: var(--teal);
    letter-spacing: -0.5px; line-height: 1;
  }
  .brand-mark {
    width: 30px; height: 30px; background: var(--teal); border-radius: 4px;
  }
  .title {
    position: absolute; top: 234px; left: 0; white-space: nowrap;
    font-size: 31px; line-height: 1.2; font-weight: 700; color: var(--heading); letter-spacing: -0.2px;
  }
  .subtitle {
    position: absolute; top: 288px; left: 0; white-space: nowrap;
    font-size: 15.5px; line-height: 18px; color: var(--muted);
  }
  .field {
    position: absolute; left: 0; width: 374px; height: 40px;
    border-bottom: 1px solid var(--line);
    font-size: 14px; color: var(--muted);
    display: flex; align-items: center;
  }
  .field--email { top: 351px; border-bottom-color: var(--line-active); }
  .field--password { top: 419px; }
  .forgot {
    position: absolute; top: 477px; right: 0; line-height: 18px;
    font-size: 14px; color: var(--teal-link); text-decoration: none;
  }
  .login-button {
    position: absolute; top: 519px; left: 0; width: 374px; height: 46px;
    border: none; border-radius: 14px; background: var(--teal);
    box-shadow: 0 3px 6px rgba(0,0,0,0.08);
    color: #fff; font: 600 15px "Inter", sans-serif;
  }
  .signup-prompt {
    position: absolute; top: 603px; left: 0; white-space: nowrap; line-height: 18px;
    font-size: 14px; color: var(--muted);
  }
  .signup-prompt a { color: var(--signup); text-decoration: none; }
  .hero-photo {
    position: absolute; left: 547px; top: 13px; width: 595px; height: 712px;
    border-radius: 35px;
    background:
      radial-gradient(ellipse at 25% 55%, rgba(120,160,200,0.55), transparent 55%),
      radial-gradient(ellipse at 80% 55%, rgba(70,90,140,0.55), transparent 50%),
      linear-gradient(180deg, #e9e4e6 0%, #d8d4d8 45%, #cdb9a3 80%, #c9c2a9 100%);
  }
</style>
</head>
<body>
  <main class="login-card">
    <section class="login-form">
      <div class="brand"><span class="brand-mark"></span>Brelvix</div>
      <h1 class="title">Welcome back!</h1>
      <p class="subtitle">Continue to your company.</p>
      <label class="field field--email">Enter your email</label>
      <label class="field field--password">Enter your password</label>
      <a class="forgot" href="#">Forgot password?</a>
      <button class="login-button" type="button">Log In</button>
      <p class="signup-prompt">Don’t have an account yet? <a href="#">Sign up</a></p>
    </section>
    <div class="hero-photo" role="img" aria-label="Photo of two colleagues talking at a table with plans and papers"></div>
  </main>
</body>
</html>
```